Kneadwell Bodycare

We are a Massage Therapy business based in Invercargill, New Zealand. We specialise in Sports and deep tissue massage but also provide relaxation and aromatherapy massage. We would like to see designs that use the the logo.
The final design should promote health and fitness.
Updates

Hi I am getting feedback that my business card picture is poor quality. I got this picture from plaza press under massage. So if you google this image a better quality picture should come up,. If not hope to upload a better image by tomorow, thanks.

Target Market(s)

Sports, people with pain and injuries

Industry/Entity Type

Massage

Requirements
Must have
• Logo, muscle body that is used on the business card, also a poster that matches my business card
Nice to have
• Picture of muscle man, shown on my business card
Should not have
• Not a picture of a real person

```html
<!DOCTYPE html>
<html lang="en">
<head>
<meta charset="utf-8">
<title>Kneadwell Bodycare – Poster</title>
<link href="https://fonts.googleapis.com/css2?family=Poppins:wght@800&family=Mulish:wght@400;700;800;900&display=swap" rel="stylesheet">
<style>
  :root {
    --page-bg: #e6e8ea;
    --sheet-top: #f6f6f8;
    --sheet-mid: #dcdee3;
    --teal: #3fb4cb;
    --teal-light: #9fd9e5;
    --teal-deep: #2a8ca3;
    --navy-top: #4a93bb;
    --navy-bottom: #143b66;
    --ink: #141414;
    --white: #ffffff;
    --address-ink: #1d4e5c;
  }
  html, body {
    margin: 0;
    width: 1200px;
    height: 1200px;
    overflow: hidden;
    background: var(--page-bg);
  }
  .poster {
    position: absolute;
    left: 204px;
    top: 40px;
    width: 792px;
    height: 1120px;
    overflow: hidden;
    background: linear-gradient(160deg, var(--sheet-top) 0%, var(--sheet-mid) 45%, var(--white) 46%);
    box-shadow: 0 10px 30px rgba(0,0,0,0.18);
    font-family: "Mulish", sans-serif;
  }
  .hero-photo {
    position: absolute;
    left: 360px;
    top: 0;
    width: 432px;
    height: 520px;
    background: radial-gradient(ellipse at 50% 45%, #c39a80 0%, #a97a60 35%, #cfcfd6 70%, #e4e5ea 100%);
  }
  .shapes {
    position: absolute;
    inset: 0;
    width: 792px;
    height: 1120px;
  }
  .headline {
    position: absolute;
    left: 42px;
    top: 70px;
    margin: 0;
    font-family: "Poppins", sans-serif;
    font-weight: 800;
    font-size: 100px;
    line-height: 0.98;
    letter-spacing: -2px;
    color: var(--ink);
  }
  .services-card {
    position: absolute;
    left: 40px;
    top: 600px;
    width: 330px;
    height: 340px;
    box-sizing: border-box;
    border: 9px solid var(--white);
    border-radius: 16px;
    background: linear-gradient(180deg, var(--navy-top) 0%, #245f8f 55%, var(--navy-bottom) 100%);
    box-shadow: 0 4px 14px rgba(0,0,0,0.25);
    padding: 26px 24px;
    color: var(--white);
  }
  .services-list {
    margin: 0;
    padding-left: 24px;
    font-weight: 800;
    font-size: 25px;
    line-height: 1.3;
  }
  .prices {
    margin: 22px 0 0 46px;
    font-size: 19px;
    line-height: 1.25;
  }
  .prices-title { font-weight: 800; }
  .services-reflection {
    position: absolute;
    left: 48px;
    top: 950px;
    width: 314px;
    height: 50px;
    border-radius: 12px;
    background: linear-gradient(180deg, rgba(200,206,220,0.6), rgba(255,255,255,0));
  }
  .brand {
    position: absolute;
    left: 400px;
    top: 610px;
    display: flex;
    align-items: center;
    gap: 18px;
  }
  .brand-name {
    margin: 0;
    font-weight: 900;
    font-size: 50px;
    line-height: 1.08;
    color: var(--teal-deep);
  }
  .brand-dot {
    flex: none;
    width: 56px;
    height: 56px;
    border-radius: 50%;
    background: var(--teal);
  }
  .phone {
    position: absolute;
    right: 40px;
    top: 955px;
    margin: 0;
    font-weight: 800;
    font-size: 44px;
    line-height: 1;
    color: var(--white);
    letter-spacing: 1px;
  }
  .practitioner {
    position: absolute;
    left: 40px;
    top: 1020px;
    margin: 0;
    font-weight: 800;
    font-size: 21px;
    line-height: 1.2;
    color: var(--white);
  }
  .address {
    position: absolute;
    left: 40px;
    top: 1076px;
    margin: 0;
    font-size: 19px;
    color: var(--address-ink);
  }
</style>
</head>
<body>
  <main class="poster">
    <div class="hero-photo" role="img" aria-label="Photo of a man seen from behind holding his lower back in pain"></div>

    <svg class="shapes" viewBox="0 0 792 1120" aria-hidden="true">
      <path d="M0,560 C250,500 520,420 792,360 L792,1120 L0,1120 Z" fill="var(--teal)"/>
      <path d="M0,578 C250,518 520,438 792,378 L792,1120 L0,1120 Z" fill="var(--teal-light)"/>
      <path d="M0,592 C250,532 520,452 792,392 L792,1120 L0,1120 Z" fill="var(--white)"/>
      <path d="M0,985 C230,930 500,920 792,830 L792,1120 L0,1120 Z" fill="var(--teal-light)"/>
      <path d="M0,1000 C240,950 510,940 792,850 L792,1120 L0,1120 Z" fill="var(--teal)"/>
    </svg>

    <h1 class="headline">Are<br>you in<br>pain?</h1>

    <section class="services-card">
      <ul class="services-list">
        <li>Deep Tissue</li>
        <li>Sports Massage</li>
        <li>Relaxation</li>
        <li>Aromatherapy</li>
        <li>Hot Stones</li>
      </ul>
      <div class="prices">
        <div class="prices-title">Prices</div>
        <div>30minutes $40</div>
        <div>60minutes $60</div>
        <div>90 minutes $80</div>
      </div>
    </section>
    <div class="services-reflection"></div>

    <div class="brand">
      <h2 class="brand-name">Kneadwell<br>Bodycare</h2>
      <span class="brand-dot"></span>
    </div>

    <p class="phone">0270481256</p>
    <p class="practitioner">Mara Ellison Bachelor Therapeutic<br>&amp; Sports massage</p>
    <p class="address">18 Fenwick St, Invercargill 9810</p>
  </main>
</body>
</html>
```